Naturopath Practitioner Card Design

I am a naturopath needing a design for a business card mainly to show that I am a naturopath and have some contact details to give to prospective clients. I am open minded about the design and what is on the second side of the card whether it just be some artwork or space for details, appointment times etc. Naturopathy is the practice of natural medicine that uses a holistic approach and incorporates herbal and nutritional medicine.

Contact Information for Business Card

Tom Waverly NaturopathBHSc (Naturopathy) Member NHPG 0491 582 736 tom.waverly@mailbox-example.net www.tomwaverlynaturopathy.example.au

Requirements
Nice to have
• Would prefer some kind of original pattern/art work/logo rather than an image, not fussed if its very simple/basic
• I am open to any colour but think I would prefer a more earthy sandy clay etc type style than the greens that are commonly associated with naturopathy.
Should not have
• Don't really want to have generic stock images on it

```html
<!DOCTYPE html>
<html lang="en">
<head>
<meta charset="utf-8">
<title>Tom Waverly Naturopath – Business Card</title>
<link rel="stylesheet" href="https://fonts.googleapis.com/css2?family=Quicksand:wght@400;500;600&display=swap">
<style>
  :root {
    --backdrop: #e3e3e3;
    --card-stock: #e9e6da;
    --card-edge: #f1efe6;
    --leaf-green: #2f7d3a;
    --leaf-deep: #1f5a2a;
    --leaf-light: #4f9a47;
    --ink: #4a4a48;
    --ink-soft: #6d6c66;
    --icon-fill: #ffffff;
  }
  * { box-sizing: border-box; margin: 0; padding: 0; }
  html, body {
    width: 1200px;
    height: 900px;
    overflow: hidden;
    background: var(--backdrop);
    font-family: "Quicksand", "Helvetica Neue", Arial, sans-serif;
  }
  .canvas {
    width: 1200px;
    height: 900px;
    display: flex;
    align-items: center;
    justify-content: center;
    gap: 60px;
  }
  .card {
    width: 500px;
    height: 286px;
    background: var(--card-stock);
    box-shadow: 0 6px 18px rgba(0, 0, 0, 0.12);
    position: relative;
  }
  /* Front: contact details */
  .card--front {
    padding: 76px 0 0 64px;
  }
  .contact-list {
    list-style: none;
    display: flex;
    flex-direction: column;
    gap: 6px;
  }
  .contact-row {
    display: flex;
    align-items: flex-start;
    gap: 10px;
    min-height: 28px;
  }
  .contact-icon {
    width: 28px;
    height: 28px;
    flex: 0 0 28px;
    background: var(--leaf-green);
    display: flex;
    align-items: center;
    justify-content: center;
  }
  .contact-icon svg { width: 16px; height: 16px; }
  .contact-name {
    font-size: 17px;
    font-weight: 600;
    color: var(--ink);
    line-height: 1.1;
  }
  .contact-title {
    font-size: 10.5px;
    font-weight: 500;
    color: var(--ink-soft);
    letter-spacing: 0.02em;
    line-height: 1.4;
  }
  .contact-value {
    font-size: 13px;
    font-weight: 500;
    color: var(--ink);
    padding-top: 6px;
    letter-spacing: 0.02em;
  }
  .contact-email {
    margin-top: 4px;
    padding-left: 38px;
    font-size: 13px;
    font-weight: 500;
    color: var(--ink);
    letter-spacing: 0.01em;
  }
  /* Back: leaf artwork */
  .card--back {
    background: var(--card-edge);
    padding: 10px;
  }
  .leaf-artwork {
    width: 100%;
    height: 100%;
    background:
      radial-gradient(circle at 30% 40%, var(--leaf-light) 0%, transparent 45%),
      radial-gradient(circle at 72% 62%, var(--leaf-light) 0%, transparent 40%),
      linear-gradient(135deg, var(--leaf-green), var(--leaf-deep));
  }
</style>
</head>
<body>
  <main class="canvas">
    <section class="card card--front" aria-label="Business card front">
      <ul class="contact-list">
        <li class="contact-row">
          <span class="contact-icon">
            <svg viewBox="0 0 16 16" aria-hidden="true">
              <circle cx="8" cy="5" r="3" fill="var(--icon-fill)"/>
              <path d="M2 15c0-3.5 2.7-5.5 6-5.5s6 2 6 5.5z" fill="var(--icon-fill)"/>
            </svg>
          </span>
          <div>
            <p class="contact-name">Tom Waverly</p>
            <p class="contact-title">Naturopath BHSc · Member NHPG</p>
          </div>
        </li>
        <li class="contact-row">
          <span class="contact-icon">
            <svg viewBox="0 0 16 16" aria-hidden="true">
              <path d="M4 1.5l2.2 3-1.4 1.6c.8 1.9 2.2 3.4 4.1 4.3l1.6-1.4 3 2.2-1.4 2.6C6.6 13.5 2.3 9.2 1.5 3z" fill="var(--icon-fill)"/>
            </svg>
          </span>
          <p class="contact-value">0491 582 736</p>
        </li>
        <li class="contact-row">
          <span class="contact-icon">
            <svg viewBox="0 0 16 16" aria-hidden="true">
              <rect x="1.5" y="3.5" width="13" height="9" fill="none" stroke="var(--icon-fill)" stroke-width="1.6"/>
              <path d="M1.5 3.5L8 9l6.5-5.5" fill="none" stroke="var(--icon-fill)" stroke-width="1.6"/>
            </svg>
          </span>
        </li>
      </ul>
      <p class="contact-email">tom.waverly@mailbox-example.net</p>
    </section>

    <section class="card card--back" aria-label="Business card back">
      <div class="leaf-artwork" role="img" aria-label="Pattern of large green monstera leaves on a cream ground"></div>
    </section>
  </main>
</body>
</html>
```